Business Card Ayurvedic Massage

I'm starting with my ayurvedic massage business and need a business card design. The design should be inline with my brand/logo as well as with the design of my website (www.mirelo-dant.ch).
Front: logo and text "Ayurvedische Massagen"
back: name and adress (see details https://www.mirelo-dant.ch/kontakt.html)

```html
<!DOCTYPE html>
<html lang="de">
<head>
<meta charset="utf-8">
<title>mirelo-dant – Visitenkarten</title>
<link rel="stylesheet" href="https://fonts.googleapis.com/css2?family=Berkshire+Swash&family=Arimo&display=swap">
<style>
  :root {
    --backdrop: #2b2d30;
    --card-red: #8e1419;
    --card-red-deep: #7a0f14;
    --gold: #f0bf4c;
    --gold-deep: #c98f25;
    --band-yellow: #fdc64b;
    --band-text: #8a1a16;
    --script: "Berkshire Swash", cursive;
    --sans: "Arimo", Arial, sans-serif;
  }
  html, body {
    margin: 0;
    width: 1200px;
    height: 900px;
    overflow: hidden;
    background: var(--backdrop);
  }
  .canvas {
    position: relative;
    width: 1200px;
    height: 900px;
  }
  .card {
    position: absolute;
    top: 269px;
    width: 560px;
    height: 362px;
    background: var(--card-red);
    overflow: hidden;
    box-shadow: 0 6px 18px rgba(0,0,0,.35);
  }
  .card--front { left: 30px; }
  .card--back  { left: 610px; }

  /* front */
  .front-pattern {
    position: absolute; inset: 0;
    background: radial-gradient(circle at 50% 45%, var(--card-red) 0%, var(--card-red-deep) 100%);
  }
  .elephant {
    position: absolute;
    border-radius: 10px;
    background: linear-gradient(160deg, var(--gold) 0%, var(--gold-deep) 55%, #b3212a 100%);
  }
  .elephant--left  { left: 40px;  top: 30px;  width: 110px; height: 110px; }
  .elephant--right { left: 410px; top: 160px; width: 120px; height: 120px; }
  .brand-name {
    position: absolute;
    left: 160px; top: 120px;
    width: 230px;
    text-align: center;
    font-family: var(--script);
    font-size: 40px;
    line-height: 1.2;
    white-space: nowrap;
    color: var(--gold);
    margin: 0;
  }
  .tagline-band {
    position: absolute;
    left: 0; right: 0; bottom: 22px;
    height: 46px;
    background: var(--band-yellow);
    display: flex; align-items: center; justify-content: center;
  }
  .tagline {
    font-family: var(--script);
    font-size: 24px;
    color: var(--band-text);
    margin: 0;
  }

  /* back */
  .back-border {
    position: absolute; inset: 14px;
    border: 14px solid var(--gold);
    opacity: .85;
  }
  .back-content {
    position: absolute; inset: 0;
    display: flex; flex-direction: column; align-items: center;
    padding-top: 74px;
    color: var(--gold);
    text-align: center;
  }
  .holder-name {
    font-family: var(--script);
    font-size: 34px;
    font-weight: 400;
    margin: 0;
  }
  .holder-role {
    display: flex; align-items: center; gap: 10px;
    font-family: var(--sans);
    font-size: 15px;
    margin: 2px 0 18px;
  }
  .holder-role svg { display: block; }
  .contact-list {
    list-style: none; margin: 0; padding: 0;
    font-family: var(--sans);
    font-size: 14px;
    line-height: 1.35;
  }
  .contact-list .gap { margin-top: 14px; }
</style>
</head>
<body>
<main class="canvas">
  <section class="card card--front">
    <div class="front-pattern" role="img" aria-label="Rotes Paisley-Muster im Hintergrund"></div>
    <div class="elephant elephant--left" role="img" aria-label="Goldener geschmückter Elefant mit Schirm"></div>
    <p class="brand-name">mirelo-dant</p>
    <div class="elephant elephant--right" role="img" aria-label="Goldener geschmückter Elefant mit Schirm"></div>
    <div class="tagline-band">
      <p class="tagline">Ayurvedische Massagen</p>
    </div>
  </section>

  <section class="card card--back">
    <div class="back-border" role="img" aria-label="Goldene Zierbordüre rund um die Karte"></div>
    <div class="back-content">
      <h1 class="holder-name">Livia Marten</h1>
      <div class="holder-role">
        <svg width="70" height="6" viewBox="0 0 70 6" aria-hidden="true"><path d="M0 3 Q35 0 70 3 Q35 6 0 3Z" fill="currentColor"/></svg>
        <span>owner</span>
        <svg width="70" height="6" viewBox="0 0 70 6" aria-hidden="true"><path d="M0 3 Q35 0 70 3 Q35 6 0 3Z" fill="currentColor"/></svg>
      </div>
      <ul class="contact-list">
        <li>info@mirelo-dant.ch</li>
        <li>+41 77 318 42 06 (Bitte keine Werbung)</li>
        <li>www.mirelo-dant.ch</li>
        <li class="gap">Studio Brenner, mirelo-dant</li>
        <li>Lindenweg 14, 8852 Altendorf (SZ)</li>
      </ul>
    </div>
  </section>
</main>
</body>
</html>
```